Leafline Nutrition

we provide nutritional consulting for loss weight and changing food habits. The clinic is promoting the life healthy, as well as natural and balanced diets that help in the control weight and for the treatment to diseases.

Reason: Waiting some desings.

Reason: Waiting some designers

Reason: Waiting for changes.

Target Market(s)

Mostly women and men aged 30-55, both with overweight, obesity and problems with your food habits.

Industry/Entity Type

Weight

Font styles to use
Script

Colors
cadf82
ffc214
b868aa
f68d4d
0393ce
33b7a4
acd037
cbdf83
eaf2cf

Requirements
Must have
• lively and natural colors
logo that evokes healthy weight, concept of healthy natural food
Nice to have
• Slim fit image with a elegant and simple design
Should not have
• Preferably not used photograps, old-Style, Boring colors

```html
<!DOCTYPE html>
<html lang="en">
<head>
<meta charset="utf-8">
<title>Leafline Nutrition – Business Card</title>
<link rel="stylesheet" href="https://fonts.googleapis.com/css2?family=Aldrich&display=swap">
<style>
  :root{
    --page-bg:#e9ebe8;
    --card-white:#ffffff;
    --card-tint:#eef0f0;
    --brand-blue:#0393ce;
    --deep-blue:#0a7fc4;
    --leaf-green:#5cae3a;
    --lime:#acd037;
    --ink:#1d1d1f;
    --shadow:rgba(0,0,0,.18);
  }
  *{margin:0;padding:0;box-sizing:border-box}
  html,body{width:1200px;height:800px;overflow:hidden;background:var(--page-bg)}
  body{font-family:"Aldrich",sans-serif;position:relative}
  .business-card{
    position:absolute;left:75px;top:100px;width:1050px;height:600px;
    background:linear-gradient(160deg,var(--card-white) 40%,var(--card-tint));
    box-shadow:0 14px 40px var(--shadow);overflow:hidden;
  }
  .accent-stripe{
    position:absolute;left:0;right:0;top:438px;height:10px;
    background:linear-gradient(90deg,var(--lime),var(--leaf-green));
  }
  .footer-band{
    position:absolute;left:0;right:0;top:456px;bottom:0;
    background:linear-gradient(90deg,var(--brand-blue),var(--deep-blue));
  }
  .brand{
    position:absolute;left:70px;top:225px;display:flex;align-items:center;gap:20px;
  }
  .brand-dot{width:46px;height:46px;border-radius:50%;background:var(--leaf-green)}
  .brand-name{font-size:52px;color:var(--brand-blue);letter-spacing:.5px}
  .contact-block{
    position:absolute;right:60px;top:55px;text-align:right;color:var(--ink);
  }
  .contact-address{font-size:25px;line-height:1.3;margin-bottom:22px}
  .contact-line{
    display:flex;justify-content:flex-end;align-items:center;gap:12px;
    font-size:21px;height:36px;
  }
  .contact-line.small{font-size:18px;height:30px}
  .contact-icon{width:22px;height:22px;flex:none}
  .holder{position:absolute;left:110px;top:490px;color:var(--card-white)}
  .holder-name{font-size:34px;letter-spacing:1.5px;text-transform:uppercase}
  .holder-role{font-size:21px;letter-spacing:1.5px;text-transform:uppercase;margin-top:6px}
</style>
</head>
<body>
<main class="business-card">
  <div class="accent-stripe"></div>
  <div class="footer-band"></div>

  <div class="brand">
    <span class="brand-dot"></span>
    <span class="brand-name">Leafline Nutrition</span>
  </div>

  <section class="contact-block">
    <p class="contact-address">41.6th floor,Plaza<br>Orchard Lane NVR</p>
    <p class="contact-line">014 672 3150
      <svg class="contact-icon" viewBox="0 0 24 24"><path d="M6 2 L10 6 L8 9 C9 12 12 15 15 16 L18 14 L22 18 L19 22 C10 21 3 14 2 5 Z" fill="var(--brand-blue)"/></svg>
    </p>
    <p class="contact-line">014 672 3150
      <svg class="contact-icon" viewBox="0 0 24 24"><rect x="6" y="1.5" width="12" height="21" rx="2" fill="none" stroke="var(--brand-blue)" stroke-width="2"/><circle cx="12" cy="19" r="1.3" fill="var(--brand-blue)"/></svg>
    </p>
    <p class="contact-line">014 672 3150
      <svg class="contact-icon" viewBox="0 0 24 24"><rect x="3" y="9" width="18" height="13" rx="1.5" fill="var(--brand-blue)"/><rect x="7" y="2" width="10" height="8" fill="none" stroke="var(--brand-blue)" stroke-width="2"/><rect x="6" y="13" width="12" height="2" fill="var(--card-white)"/></svg>
    </p>
    <p class="contact-line small">hello@leafline.com
      <svg class="contact-icon" viewBox="0 0 24 24"><rect x="2" y="5" width="20" height="14" rx="1.5" fill="var(--brand-blue)"/><path d="M2 6 L12 13 L22 6" fill="none" stroke="var(--card-white)" stroke-width="1.8"/></svg>
    </p>
    <p class="contact-line small">www.leaflinenutrition.com
      <svg class="contact-icon" viewBox="0 0 24 24"><circle cx="12" cy="12" r="10" fill="none" stroke="var(--brand-blue)" stroke-width="2"/><ellipse cx="12" cy="12" rx="4.5" ry="10" fill="none" stroke="var(--brand-blue)" stroke-width="1.6"/><path d="M2 12 H22 M4 7 H20 M4 17 H20" stroke="var(--brand-blue)" stroke-width="1.4"/></svg>
    </p>
  </section>

  <div class="holder">
    <p class="holder-name">Daniel Reyes</p>
    <p class="holder-role">Wellness Advisor</p>
  </div>
</main>
</body>
</html>
```